Verdant Ledger - Paid Surveys publisher portal

• Homepage
• Blank Sub Page (Where content goes in between the header/footer)
• Publisher Application Page, complete with Form
• Survey Wall page

Sites that are in a similar vertical that have interesting designs:
mobrivex.com
tandulo.com
vorql.com
pim.ox

This is a business-to-business site, and needs to have this type of feel to it. Focus on generating revenue, offer completion, paid surveys is the market.

Format: HTML/CSS

Link to current version of application, and form:
https://quorbit.travenlo.com
https://quorbit.travenlo.com/apply
https://quorbit.travenlo.com/panel/4/mirvak_user

Please note that we are changing the brand of this project, the name will be determined shortly but everything else remains. It will likely be Verdant Ledger instead of Quorbit. We will confirm.

Industry/Entity Type

Market Research

Coding

Coded - Design and coding required

Number of Pages Required

4 page

Font styles to use
Sans Serif

Colors

Designer to choose colors to be used in the design.

```html
<!DOCTYPE html>
<html lang="en">
<head>
<meta charset="utf-8">
<title>Quorbit – Paid Surveys Publisher Portal</title>
<link href="https://fonts.googleapis.com/css2?family=Poppins:wght@400;500;600;700&family=Montserrat:wght@400;500;600&display=swap" rel="stylesheet">
<style>
:root{
  --nav:#262b36;
  --coral:#f0604f;
  --blue:#2d9ad6;
  --ink:#222630;
  --body:#3a3d44;
  --card:#f2f2f2;
  --white:#ffffff;
  --rule:#d6d6d6;
  --stat1:#1b7cb8;
  --stat2:#2590cf;
  --stat3:#2c9bd9;
  --stat4:#4db1e6;
  --stat5:#73c7ee;
}
*{margin:0;padding:0;box-sizing:border-box}
html,body{width:1200px;height:2632px;overflow:hidden}
body{position:relative;background:var(--white);font-family:"Montserrat",Arial,sans-serif;color:var(--body)}
a{color:inherit;text-decoration:none}

.site-header{position:absolute;left:0;top:0;width:1200px;height:62px;background:var(--nav);border-bottom:2px solid #c9ccd2;z-index:3}
.brand{position:absolute;left:98px;top:14px;display:flex;align-items:center;gap:12px;color:var(--white);font-family:"Poppins",sans-serif;font-weight:500;font-size:25px}
.brand-dot{width:34px;height:34px;border-radius:50%;background:var(--coral)}
.main-nav{position:absolute;right:98px;top:19px;display:flex;gap:47px;font-family:"Poppins",sans-serif;font-weight:500;font-size:17px;color:var(--white)}

.hero{position:absolute;left:0;top:62px;width:1200px;height:640px;background:radial-gradient(ellipse 900px 380px at 600px 700px,#3a5a86 0%,#1c2b4a 45%,#0d1427 75%,#070b18 100%)}
.hero-title{position:absolute;left:0;top:82px;width:100%;text-align:center;color:var(--white);font-family:"Poppins",sans-serif;font-weight:700;font-size:43px}
.hero-sub{position:absolute;left:200px;top:152px;width:800px;text-align:center;color:var(--white);font-family:"Poppins",sans-serif;font-size:19px;line-height:30px}
.feature{position:absolute;top:275px;width:330px}
.feature-head{height:66px;line-height:66px;text-align:center;color:var(--white);font-family:"Poppins",sans-serif;font-weight:500;font-size:21px}
.feature-body{margin-top:9px;height:202px;background:var(--card);text-align:center;padding:30px 22px 0}
.feature-body p{font-size:14.5px;line-height:24px;color:var(--ink)}
.btn{display:inline-block;color:var(--white);font-family:"Poppins",sans-serif;font-size:15px;border-radius:4px;text-align:center}
.feature .btn{margin-top:20px;width:108px;height:44px;line-height:44px}
.coral{background:var(--coral)}
.blue{background:var(--blue)}

.stats{position:absolute;left:0;top:702px;width:1200px;height:151px;display:flex}
.stat{width:240px;color:var(--white);text-align:center;padding-top:40px}
.stat-num{font-family:"Poppins",sans-serif;font-weight:600;font-size:30px;line-height:40px}
.stat-label{font-family:"Poppins",sans-serif;font-weight:500;font-size:15px;margin-top:8px}

.photo{position:absolute}
.story{position:absolute;width:510px}
.story-date{font-family:"Poppins",sans-serif;font-weight:600;font-size:16px;color:var(--ink)}
.story-title{margin-top:16px;font-family:"Poppins",sans-serif;font-weight:500;font-size:24px;line-height:29px;color:var(--blue)}
.story-text{margin-top:14px;font-size:14.5px;line-height:23px;text-align:justify;color:var(--ink)}
.story .btn{margin-top:30px;width:108px;height:43px;line-height:43px}

.banner{position:absolute;left:0;top:1728px;width:1200px;height:480px;background:linear-gradient(135deg,#e8e6e2 0%,#cfc9c0 40%,#a9a39c 70%,#7f7a78 100%)}
.banner-box{position:absolute;left:98px;top:66px;width:490px;height:348px;background:rgba(255,255,255,.82);padding:38px 30px}
.banner-title{font-family:"Poppins",sans-serif;font-weight:500;font-size:27px;line-height:31px;color:var(--coral)}
.banner-text{margin-top:28px;font-size:14.5px;line-height:24px;text-align:justify;color:var(--ink)}
.banner .btn{margin-top:26px;width:108px;height:43px;line-height:43px}

.site-footer{position:absolute;left:0;top:2208px;width:1200px;height:424px}
.footer-brand{position:absolute;left:98px;top:165px;display:flex;align-items:center;gap:12px;font-family:"Poppins",sans-serif;font-weight:500;font-size:25px;color:var(--ink)}
.footer-brand .brand-dot{width:54px;height:54px}
.footer-col{position:absolute;top:78px}
.footer-col h3{font-family:"Poppins",sans-serif;font-weight:600;font-size:18px;color:var(--coral);margin-bottom:14px}
.footer-col li{list-style:none;display:flex;align-items:center;gap:16px;font-size:14px;font-weight:500;height:27.4px;color:var(--ink)}
.footer-col li svg{flex:none}
.news-text{font-size:14px;font-weight:500;line-height:20px;color:var(--ink);width:270px}
.news-input{margin-top:14px;width:265px;height:38px;border:2px solid #7c7f86;border-radius:6px;padding-left:12px;line-height:34px;font-size:14px;color:var(--ink)}
.news-btn{margin-top:14px;width:100px;height:38px;line-height:38px;font-size:14px;font-weight:500;font-family:"Montserrat",sans-serif}
.footer-rule{position:absolute;left:98px;top:346px;width:1004px;height:1px;background:var(--rule)}
.copyright{position:absolute;left:0;top:376px;width:100%;text-align:center;font-family:"Poppins",sans-serif;font-weight:500;font-size:15.5px;color:var(--ink)}
</style>
</head>
<body>

<header class="site-header">
  <a class="brand" href="#"><span class="brand-dot"></span>Quorbit</a>
  <nav class="main-nav">
    <a href="#">Home</a><a href="#">Survey</a><a href="#">Revenue</a><a href="#">Monetize</a><a href="#">Contact Us</a><a href="#">Login</a>
  </nav>
</header>

<section class="hero" role="img" aria-label="Night view of Earth from space with glowing city lights">
  <h1 class="hero-title">Welcome To Quorbit</h1>
  <p class="hero-sub">We are a B2B company focussing on generating revenue, offer completion, paid surveys is the market.</p>

  <div class="feature" style="left:98px">
    <div class="feature-head coral">Generating Revenue</div>
    <div class="feature-body"><p>Duis aute irure dolor in reprehenderit in voluptate velit esse cillum dolore eu fugiat nulla pariatur.</p><a class="btn coral" href="#">Read More</a></div>
  </div>
  <div class="feature" style="left:435px">
    <div class="feature-head blue">Offer Completion</div>
    <div class="feature-body"><p>Duis aute irure dolor in reprehenderit in voluptate velit esse cillum dolore eu fugiat nulla pariatur.</p><a class="btn blue" href="#">Read More</a></div>
  </div>
  <div class="feature" style="left:772px">
    <div class="feature-head coral">Paid Surveys</div>
    <div class="feature-body"><p>Duis aute irure dolor in reprehenderit in voluptate velit esse cillum dolore eu fugiat nulla pariatur.</p><a class="btn coral" href="#">Read More</a></div>
  </div>
</section>

<section class="stats">
  <div class="stat" style="background:var(--stat1)"><div class="stat-num">20,000,000</div><div class="stat-label">Registered Consumers</div></div>
  <div class="stat" style="background:var(--stat2)"><div class="stat-num">2,500</div><div class="stat-label">Community Owners</div></div>
  <div class="stat" style="background:var(--stat3)"><div class="stat-num">100+</div><div class="stat-label">Countries Reached</div></div>
  <div class="stat" style="background:var(--stat4)"><div class="stat-num">250,000</div><div class="stat-label">New Members Each Day</div></div>
  <div class="stat" style="background:var(--stat5)"><div class="stat-num">660+</div><div class="stat-label">Offer Completion</div></div>
</section>

<div class="photo" style="left:98px;top:937px;width:446px;height:328px;background:linear-gradient(120deg,#3b3a3c 0%,#6d655f 40%,#b9aea4 70%,#57514e 100%)" role="img" aria-label="Three colleagues reviewing a tablet together at a cafe table"></div>
<article class="story" style="left:593px;top:978px">
  <div class="story-date">August 23, 2018</div>
  <h2 class="story-title">B2B company focussing on generating revenue</h2>
  <p class="story-text">Nemo enim ipsam voluptatem quia voluptas sit aspernatur aut odit aut fugit, sed quia consequuntur magni dolores eos qui ratione voluptatem sequi nesciunt.</p>
  <a class="btn blue" href="#">Read More</a>
</article>

<article class="story" style="left:98px;top:1356px">
  <div class="story-date">February 16, 2018</div>
  <h2 class="story-title">B2B company focussing on offer completion</h2>
  <p class="story-text">Nemo enim ipsam voluptatem quia voluptas sit aspernatur aut odit aut fugit, sed quia consequuntur magni dolores eos qui ratione voluptatem sequi nesciunt.</p>
  <a class="btn blue" href="#">Read More</a>
</article>
<div class="photo" style="left:656px;top:1314px;width:446px;height:328px;background:linear-gradient(120deg,#c9a58a 0%,#b8785a 35%,#d9c2ad 65%,#8f5c4c 100%)" role="img" aria-label="Colleagues smiling while signing a document at a table"></div>

<section class="banner" role="img" aria-label="Team meeting around a bright office table seen from above">
  <div class="banner-box">
    <h2 class="banner-title">We are a paid surveys publisher portal</h2>
    <p class="banner-text">Sed ut perspiciatis unde omnis iste natus error sit voluptatem accusantium doloremque laudantium, totam rem aperiam, eaque ipsa quae ab illo inventore veritatis et quasi architecto beatae vitae dicta sunt explicabo.</p>
    <a class="btn blue" href="#">Read More</a>
  </div>
</section>

<footer class="site-footer">
  <div class="footer-brand"><span class="brand-dot"></span>Quorbit</div>

  <div class="footer-col" style="left:386px">
    <h3>QUICK LINKS</h3>
    <ul>
      <li><svg width="14" height="12" viewBox="0 0 14 12"><path d="M1 6h10M7 2l4 4-4 4" fill="none" stroke="#222630" stroke-width="1.6"/></svg>Home</li>
      <li><svg width="14" height="12" viewBox="0 0 14 12"><path d="M1 6h10M7 2l4 4-4 4" fill="none" stroke="#222630" stroke-width="1.6"/></svg>Survey</li>
      <li><svg width="14" height="12" viewBox="0 0 14 12"><path d="M1 6h10M7 2l4 4-4 4" fill="none" stroke="#222630" stroke-width="1.6"/></svg>Revenue</li>
      <li><svg width="14" height="12" viewBox="0 0 14 12"><path d="M1 6h10M7 2l4 4-4 4" fill="none" stroke="#222630" stroke-width="1.6"/></svg>Monetize</li>
      <li><svg width="14" height="12" viewBox="0 0 14 12"><path d="M1 6h10M7 2l4 4-4 4" fill="none" stroke="#222630" stroke-width="1.6"/></svg>Contact Us</li>
      <li><svg width="14" height="12" viewBox="0 0 14 12"><path d="M1 6h10M7 2l4 4-4 4" fill="none" stroke="#222630" stroke-width="1.6"/></svg>Login</li>
    </ul>
  </div>

  <div class="footer-col" style="left:617px">
    <h3>SOCIAL MEDIA</h3>
    <ul>
      <li><svg width="12" height="12"><circle cx="6" cy="6" r="5" fill="#222630"/></svg>Chatterbox</li>
      <li><svg width="12" height="12"><circle cx="6" cy="6" r="5" fill="#222630"/></svg>Quillpost</li>
      <li><svg width="12" height="12"><circle cx="6" cy="6" r="5" fill="#222630"/></svg>Orbnet</li>
      <li><svg width="12" height="12"><circle cx="6" cy="6" r="5" fill="#222630"/></svg>Pinboardly</li>
      <li><svg width="12" height="12"><circle cx="6" cy="6" r="5" fill="#222630"/></svg>Snapfold</li>
      <li><svg width="12" height="12"><circle cx="6" cy="6" r="5" fill="#222630"/></svg>Reelhub</li>
    </ul>
  </div>

  <div class="footer-col" style="left:837px">
    <h3>NEWSLETTER</h3>
    <p class="news-text">Duis aute irure dolor in reprehenderit in voluptate velit esse</p>
    <div class="news-input">Email Address</div>
    <div class="btn blue news-btn">SUBSCRIBE</div>
  </div>

  <div class="footer-rule"></div>
  <p class="copyright">Copyrights @ 2018 Quorbit. All Rights Reserved.</p>
</footer>

</body>
</html>
```